We need business cards for our Kashmiri Indian Takeaway Shop. our business sells authentic Kashmiri Cuisine. We also offer catering services and have a BYO Function Room available for private bookings. We would like to see simple but stylish designs that feature Moroccan or Arabic style patterns/ borders and use golds, deep reds, pearl/cream and a touch of black or white. We do not want pictures of curries or Indian spices, chillies etc. The final design should communicate sumptuous, exotic dining.

Target Market(s)

Indian food lovers

Industry/Entity Type

Catering

Contact Information for Business Card

Rafiq's Kitchen Authentic Kashmiri Indian Cuisine

Colors
ec2027
fce8d3
fcca95
faa54b

Requirements
Must have
• Simple but stylish design, using Moroccan/Arabic inspired borders or features
Should not have
• Pictures of curries, spices, food etc

```html
<!DOCTYPE html>
<html lang="en">
<head>
<meta charset="utf-8">
<title>Rafiq's Kitchen – Business Card</title>
<link href="https://fonts.googleapis.com/css2?family=Cinzel:wght@400;600;700&display=swap" rel="stylesheet">
<style>
  :root {
    --backdrop: #ece6dd;
    --card-red: #c0141c;
    --card-red-deep: #8e0c12;
    --card-red-light: #ec2027;
    --gold: #faa54b;
    --gold-soft: #fcca95;
    --cream: #fce8d3;
    --gold-dark: #b9772a;
  }
  * { box-sizing: border-box; margin: 0; padding: 0; }
  html, body {
    width: 1200px; height: 1023px; overflow: hidden;
    background: var(--backdrop);
  }
  .canvas {
    width: 1200px; height: 1023px;
    display: flex; align-items: center; justify-content: center;
  }
  .business-card {
    position: relative;
    width: 900px; height: 514px;
    border-radius: 6px;
    overflow: hidden;
    background: radial-gradient(ellipse at 62% 45%, var(--card-red-light) 0%, var(--card-red) 45%, var(--card-red-deep) 100%);
    box-shadow: 0 18px 40px rgba(60, 20, 10, 0.3);
    font-family: "Cinzel", "Times New Roman", serif;
    font-variant: small-caps;
  }
  .damask-ornament {
    position: absolute;
    left: -110px; top: 62px;
    width: 390px; height: 390px;
    border-radius: 50%;
    background: radial-gradient(circle, rgba(252,202,149,0.85) 0%, rgba(250,165,75,0.6) 45%, rgba(185,119,42,0.35) 75%, rgba(185,119,42,0) 100%);
  }
  .card-content {
    position: absolute;
    left: 330px; right: 40px; top: 0; bottom: 0;
    display: flex; flex-direction: column; align-items: center;
    text-align: center;
  }
  .brand-name {
    margin-top: 52px;
    font-size: 46px; font-weight: 600; letter-spacing: 1px;
    color: var(--cream);
  }
  .brand-tagline {
    margin-top: 4px;
    font-size: 19px; letter-spacing: 1px;
    color: var(--gold-soft);
  }
  .scroll-flourish {
    margin-top: 18px;
    width: 170px; height: 72px;
    border-radius: 36px;
    background: linear-gradient(90deg, rgba(250,165,75,0.25), rgba(252,202,149,0.75), rgba(250,165,75,0.25));
  }
  .owner-name {
    margin-top: 24px;
    font-size: 32px; font-weight: 700;
    color: var(--gold);
  }
  .owner-role {
    margin-top: 2px;
    font-size: 17px;
    color: var(--cream);
  }
  .gold-rule {
    margin-top: 14px;
    width: 200px; height: 2px;
    background: linear-gradient(90deg, transparent, var(--gold), transparent);
  }
  .phone-line {
    margin-top: 14px;
    display: flex; align-items: center; gap: 8px;
    font-size: 18px; color: var(--cream);
    font-variant: normal;
  }
  .phone-icon { width: 18px; height: 18px; }
  .address-label {
    margin-top: 26px;
    font-size: 17px; font-weight: 600;
    color: var(--gold);
  }
  .address-lines {
    margin-top: 6px;
    font-size: 17px; line-height: 1.45;
    color: var(--cream);
  }
</style>
</head>
<body>
  <main class="canvas">
    <article class="business-card">
      <div class="damask-ornament" role="img" aria-label="Gold floral damask ornament"></div>
      <div class="card-content">
        <h1 class="brand-name">Rafiq's Kitchen</h1>
        <p class="brand-tagline">Authentic Kashmiri Indian Cuisine</p>
        <div class="scroll-flourish" role="img" aria-label="Gold calligraphic scroll flourish"></div>
        <h2 class="owner-name">Samir Qadri</h2>
        <p class="owner-role">Owner &amp; Chef</p>
        <div class="gold-rule"></div>
        <p class="phone-line">
          <svg class="phone-icon" viewBox="0 0 18 18" aria-hidden="true">
            <rect width="18" height="18" rx="3" fill="#faa54b"/>
            <path d="M5.5 4.5c.6-.4 1.2-.3 1.5.3l.9 1.6c.2.5.1 1-.3 1.3l-.6.5c.5 1.2 1.4 2.1 2.6 2.7l.5-.6c.3-.4.8-.5 1.3-.3l1.6.9c.6.3.7.9.3 1.5-.7 1-1.8 1.3-3 .8-2.4-1-4.2-2.8-5.2-5.2-.5-1.2-.2-2.3.4-3.5z" fill="#8e0c12"/>
          </svg>
          07- 4000 1234
        </p>
        <p class="address-label">Kashmiri Address:</p>
        <p class="address-lines">14B Harbour Lane, Millbrook QLD Takeaways,<br>Catering &amp; BYO Function Room</p>
      </div>
    </article>
  </main>
</body>
</html>
```